K.O.V Ventures - Business Card

We need a business card design for a new company based in Malaysia, called K.O.V Ventures Sdn. Bhd. We create, develop & customize database & software/web-based business systems to suit our clients need, mainly in oil&gas industry.

We would like to challenge the creativity of you to design a simple, meaningful, modern, professional & sleek. The design concept may varies but worthy enough for the recipients to proudly keep it in their wallet, and award us with fruitful business opportunities.

B-7-12 Lantera Plaza,
PJU9/4, Damai Perdana,
47500 Selangor. Malaysia

http://kovventures-example.com

HAFIZ Rosman | +6012-7038812 | Co-Founder
Di Kamarul | +6012-4190273 | Co-Founder
Amir Syukri | +6019-3306158 | Managing Director

Target Market(s)

The target market will expand to several other industries such as aviation, communication, automotive, education & hotel.

Industry/Entity Type

Business

Font styles to use
Serif
Sans Serif
Decorative
Script

Requirements
Must have
• plain background yet colourful concept.
Should not have
• something too easy that I can draw myself

```html
<!DOCTYPE html>
<html lang="en">
<head>
<meta charset="utf-8">
<title>K.O.V Ventures - Business Card</title>
<link rel="stylesheet" href="https://fonts.googleapis.com/css2?family=Roboto:wght@300;400;700;900&family=Roboto+Condensed:wght@400&display=swap">
<style>
  :root {
    --stage: #e4e5e7;
    --stage-light: #f4f4f5;
    --blue-deep: #0b4d66;
    --blue-bright: #00a6c6;
    --blue-ink: #0d5670;
    --red-deep: #560006;
    --red-bright: #e31b25;
    --red-ink: #6a0a0e;
    --white: #ffffff;
    --paper-a: #e8e9ea;
    --paper-b: #fbfbfb;
    --paper-edge: #b7b8ba;
  }
  * { margin: 0; padding: 0; box-sizing: border-box; }
  html, body { width: 1200px; height: 900px; overflow: hidden; }
  body {
    background: radial-gradient(ellipse at 50% 45%, var(--stage-light) 0%, var(--stage) 75%);
    font-family: "Roboto", Arial, sans-serif;
    position: relative;
  }
  .card-set { position: absolute; left: 262px; width: 696px; height: 386px; }
  .card-set--blue { top: 32px; --ink: var(--blue-ink); --deep: var(--blue-deep); --bright: var(--blue-bright); }
  .card-set--red { top: 460px; --ink: var(--red-ink); --deep: var(--red-deep); --bright: var(--red-bright); }

  .card-back {
    position: absolute; left: 0; top: 0; width: 328px; height: 386px;
    background: linear-gradient(180deg, var(--deep) 0%, var(--bright) 48%, var(--deep) 100%);
    box-shadow: 0 8px 10px -6px rgba(0,0,0,.35);
    color: var(--white);
  }
  .card-set--red .card-back {
    background: linear-gradient(180deg, var(--deep) 0%, #7a0008 25%, var(--bright) 50%, #7a0008 75%, var(--deep) 100%);
  }
  .card-back__url {
    position: absolute; top: 7px; left: 0; width: 100%; text-align: center;
    font-size: 15px; letter-spacing: 4.6px; font-weight: 400; white-space: nowrap;
  }
  .brand { position: absolute; left: 26px; top: 150px; display: flex; align-items: center; gap: 12px; }
  .brand__dot { width: 44px; height: 44px; border-radius: 50%; background: var(--white); opacity: .85; }
  .brand__name { font-size: 68px; font-weight: 900; line-height: 1; color: var(--white); letter-spacing: -1px; }
  .brand__tagline {
    position: absolute; left: 120px; top: 229px; font-size: 8.5px; font-weight: 400; letter-spacing: .1px; white-space: nowrap;
  }
  .social {
    position: absolute; left: 10px; bottom: 12px; display: flex; align-items: center;
    font-size: 15px; letter-spacing: -.3px;
  }
  .social__item { display: flex; align-items: center; gap: 5px; padding: 0 7px; }
  .social__item + .social__item { border-left: 1px solid rgba(255,255,255,.8); }
  .social__mark { width: 18px; height: 18px; border-radius: 50%; background: var(--white); }

  .card-front {
    position: absolute; left: 328px; top: 0; width: 368px; height: 386px;
    background: linear-gradient(90deg, var(--paper-a) 0%, var(--paper-b) 35%, #f0f0f1 70%, var(--paper-edge) 100%);
    box-shadow: 0 8px 10px -6px rgba(0,0,0,.3);
    color: var(--ink);
  }
  .band { position: absolute; left: 75px; width: 219px; background: var(--ink); }
  .band--top { top: 0; height: 56px; }
  .band--bottom { bottom: 0; height: 18px; }
  .person { position: absolute; top: 94px; left: 75px; width: 219px; text-align: center; }
  .person__name { font-size: 36px; font-weight: 300; letter-spacing: -1px; white-space: nowrap; line-height: 1; display: block; }
  .person__role { font-size: 18.5px; font-weight: 400; display: block; margin-top: 6px; }
  .contact { position: absolute; font-size: 14.5px; white-space: nowrap; }
  .icon { position: absolute; }
  .phone-office { left: 82px; top: 265px; }
  .phone-mobile { left: 192px; top: 265px; }
  .email { left: 105px; top: 292px; font-size: 15px; letter-spacing: .2px; }
  .address { left: 103px; top: 322px; font-family: "Roboto Condensed", "Arial Narrow", sans-serif; font-size: 15.5px; line-height: 24px; letter-spacing: -.3px; }
  .address span { display: block; }
</style>
</head>
<body>

<section class="card-set card-set--blue">
  <div class="card-back">
    <p class="card-back__url">www.kovgroup-example.com</p>
    <div class="brand"><span class="brand__dot"></span><span class="brand__name">K.O.V</span></div>
    <p class="brand__tagline">DATABASE &amp; BUSINESS SYSTEM SOLUTIONS</p>
    <div class="social">
      <span class="social__item"><span class="social__mark"></span>@hafiz</span>
      <span class="social__item"><span class="social__mark"></span>in/hafiz</span>
      <span class="social__item"><span class="social__mark"></span>hafiz</span>
    </div>
  </div>
  <div class="card-front">
    <div class="band band--top"></div>
    <div class="person"><span class="person__name">Hafiz Rosman</span><span class="person__role">Director Sales</span></div>
    <svg class="icon" style="left:118px;top:236px" width="24" height="24" viewBox="0 0 24 24"><circle cx="12" cy="12" r="10.5" fill="none" stroke="var(--ink)" stroke-width="2"/><path d="M8.5 6.5l2 2.4-1.2 1.3c.7 1.6 2 2.9 3.5 3.6l1.3-1.2 2.4 2-1.2 1.9c-4.2-.6-7.8-4.2-8.3-8.4z" fill="var(--ink)"/></svg>
    <svg class="icon" style="left:231px;top:235px" width="16" height="26" viewBox="0 0 16 26"><rect x="1.5" y="1.5" width="13" height="23" rx="2" fill="none" stroke="var(--ink)" stroke-width="2"/><rect x="4" y="4.5" width="8" height="14" fill="var(--ink)"/><circle cx="8" cy="21.5" r="1.3" fill="var(--ink)"/></svg>
    <span class="contact phone-office">021-555-0187</span>
    <span class="contact phone-mobile">992-555-0142</span>
    <svg class="icon" style="left:76px;top:294px" width="22" height="15" viewBox="0 0 22 15"><rect width="22" height="15" rx="1.5" fill="var(--ink)"/><path d="M1 1.5l10 7 10-7" fill="none" stroke="#fff" stroke-width="1.6"/></svg>
    <span class="contact email">hafiz@kovventures-example.com</span>
    <svg class="icon" style="left:78px;top:320px" width="18" height="28" viewBox="0 0 18 28"><path d="M9 1.5a7.5 7.5 0 0 0-7.5 7.5C1.5 15 9 26 9 26s7.5-11 7.5-17A7.5 7.5 0 0 0 9 1.5z" fill="none" stroke="var(--ink)" stroke-width="2.4"/><circle cx="9" cy="9" r="2.6" fill="var(--ink)"/></svg>
    <p class="contact address"><span>22 Lantera Crescent Parkland</span><span>PJ9 4DP Kuala Lumpur</span></p>
    <div class="band band--bottom"></div>
  </div>
</section>

<section class="card-set card-set--red">
  <div class="card-back">
    <p class="card-back__url">www.kovgroup-example.com</p>
    <div class="brand"><span class="brand__dot"></span><span class="brand__name">K.O.V</span></div>
    <p class="brand__tagline">DATABASE &amp; BUSINESS SYSTEM SOLUTIONS</p>
    <div class="social">
      <span class="social__item"><span class="social__mark"></span>@hafiz</span>
      <span class="social__item"><span class="social__mark"></span>in/hafiz</span>
      <span class="social__item"><span class="social__mark"></span>hafiz</span>
    </div>
  </div>
  <div class="card-front">
    <div class="band band--top"></div>
    <div class="person"><span class="person__name">Hafiz Rosman</span><span class="person__role">Director Sales</span></div>
    <svg class="icon" style="left:118px;top:236px" width="24" height="24" viewBox="0 0 24 24"><circle cx="12" cy="12" r="10.5" fill="none" stroke="var(--ink)" stroke-width="2"/><path d="M8.5 6.5l2 2.4-1.2 1.3c.7 1.6 2 2.9 3.5 3.6l1.3-1.2 2.4 2-1.2 1.9c-4.2-.6-7.8-4.2-8.3-8.4z" fill="var(--ink)"/></svg>
    <svg class="icon" style="left:231px;top:235px" width="16" height="26" viewBox="0 0 16 26"><rect x="1.5" y="1.5" width="13" height="23" rx="2" fill="none" stroke="var(--ink)" stroke-width="2"/><rect x="4" y="4.5" width="8" height="14" fill="var(--ink)"/><circle cx="8" cy="21.5" r="1.3" fill="var(--ink)"/></svg>
    <span class="contact phone-office">021-555-0187</span>
    <span class="contact phone-mobile">992-555-0142</span>
    <svg class="icon" style="left:76px;top:294px" width="22" height="15" viewBox="0 0 22 15"><rect width="22" height="15" rx="1.5" fill="var(--ink)"/><path d="M1 1.5l10 7 10-7" fill="none" stroke="#fff" stroke-width="1.6"/></svg>
    <span class="contact email">hafiz@kovventures-example.com</span>
    <svg class="icon" style="left:78px;top:320px" width="18" height="28" viewBox="0 0 18 28"><path d="M9 1.5a7.5 7.5 0 0 0-7.5 7.5C1.5 15 9 26 9 26s7.5-11 7.5-17A7.5 7.5 0 0 0 9 1.5z" fill="none" stroke="var(--ink)" stroke-width="2.4"/><circle cx="9" cy="9" r="2.6" fill="var(--ink)"/></svg>
    <p class="contact address"><span>22 Lantera Crescent Parkland</span><span>PJ9 4DP Kuala Lumpur</span></p>
    <div class="band band--bottom"></div>
  </div>
</section>

</body>
</html>
```